Pipelining Product Supply Company Needs New Stationery

We need new stationery (letter head, with compliments slips & business card) for our industry leading pipe lining supply company. basically we sell product to other plumbers to carry out pipe relining.

Im looking for something, fresh, professional, sleek and modern at the same time.

Ive attached a copy of the logo and also some guidelines to follow for colours and fonts etc.

Target Market(s)

Plumbers

Industry/Entity Type

Plumbing

Font styles to use
Sans Serif

Requirements
Must have
• The logo, space for ABN, Address, Phone Number, website and email.
Nice to have
• Stand out from the crowd. To look sleep and professional.
Should not have
• Any other colours apart from what is on the guidelines.

```html
<!DOCTYPE html>
<html lang="en">
<head>
<meta charset="utf-8">
<title>Norvale Pipeline Supplies – Business Card</title>
<link rel="stylesheet" href="https://fonts.googleapis.com/css2?family=Josefin+Sans:wght@300;400&family=Open+Sans:wght@700&display=swap">
<style>
  :root {
    --backdrop: #a7c48b;
    --green-deep: #5b8a2a;
    --green-mid: #7fb040;
    --green-light: #bde77f;
    --accent: #8cc63f;
    --paper: #ffffff;
    --ink: #4a4a4a;
  }
  * { margin: 0; padding: 0; box-sizing: border-box; }
  html, body { width: 1200px; height: 914px; overflow: hidden; }
  body {
    background: var(--backdrop);
    display: flex;
    align-items: center;
    justify-content: center;
    gap: 64px;
    font-family: "Josefin Sans", sans-serif;
  }
  .card { box-shadow: 0 18px 40px rgba(40, 70, 20, 0.28); position: relative; }

  /* back: contact side */
  .card-back {
    width: 540px; height: 308px;
    background: var(--paper);
    padding: 46px 52px;
    display: flex; flex-direction: column; justify-content: space-between;
  }
  .card-back .brand-name {
    display: flex; align-items: center; gap: 12px;
    color: var(--accent); font-weight: 400; font-size: 28px; letter-spacing: 1px;
  }
  .brand-dot { width: 14px; height: 14px; border-radius: 50%; background: currentColor; flex: none; }
  .contact-list { list-style: none; color: var(--ink); font-weight: 300; font-size: 16px; line-height: 1.75; }
  .contact-list li { display: flex; align-items: flex-start; gap: 12px; }
  .contact-list svg { width: 14px; height: 14px; margin-top: 5px; flex: none; fill: var(--accent); }
  .contact-list .indent { padding-left: 26px; }

  /* front: name side */
  .card-front {
    width: 308px; height: 540px;
    background: linear-gradient(115deg, var(--green-deep) 0%, var(--green-mid) 45%, var(--green-light) 100%);
    color: var(--paper);
    display: flex; flex-direction: column; align-items: center; text-align: center;
    padding: 150px 24px 0;
  }
  .card-front .brand-name {
    display: flex; flex-direction: column; align-items: center; gap: 10px;
    font-weight: 400; font-size: 26px; letter-spacing: 1px; line-height: 1.15;
  }
  .person { margin-top: 150px; }
  .person-name { font-family: "Open Sans", sans-serif; font-weight: 700; font-size: 19px; }
  .person-role { font-weight: 300; font-size: 15px; font-variant: small-caps; letter-spacing: 0.5px; margin-top: 6px; }
</style>
</head>
<body>
  <section class="card card-back">
    <div class="brand-name"><span class="brand-dot"></span>Norvale Pipeline Supplies</div>
    <ul class="contact-list">
      <li><svg viewBox="0 0 14 14"><path d="M7 0a5 5 0 0 0-5 5c0 4 5 9 5 9s5-5 5-9a5 5 0 0 0-5-5zm0 7a2 2 0 1 1 0-4 2 2 0 0 1 0 4z"/></svg>12 Sample Street, Suite 0000</li>
      <li class="indent">Geelong, VIC 3220</li>
      <li><svg viewBox="0 0 14 14"><path d="M3 0l3 3-1.5 2a8 8 0 0 0 4.5 4.5L11 8l3 3-2 3C6 14 0 8 0 2z"/></svg>(000) 000-4815</li>
      <li><svg viewBox="0 0 14 14"><path d="M0 3h14v8H0zM1 4l6 4 6-4" stroke="#fff" stroke-width="1"/></svg>contact@norvalepipe.com.au</li>
      <li><svg viewBox="0 0 14 14"><circle cx="7" cy="7" r="6.5"/><path d="M1 7h12M7 1c-3 3-3 9 0 12M7 1c3 3 3 9 0 12" stroke="#fff" stroke-width="1" fill="none"/></svg>www.norvalepipe.com.au</li>
    </ul>
  </section>

  <section class="card card-front">
    <div class="brand-name"><span class="brand-dot"></span>Norvale<br>Pipeline Supplies</div>
    <div class="person">
      <p class="person-name">Example Name</p>
      <p class="person-role">Designation</p>
    </div>
  </section>
</body>
</html>
```